Flyer Advertising Summer Programs for students - 6x9 inches

We need a 6x9 front and back flyer to advertise our summer programs. We are an interfaith organization that does programs with youth of all religious and non-religious backgrounds. I've sent our logos, copy, pictures, etc. that you can work with to make it pop!

Target Market(s)

youth and their parents and religious communities

Industry/Entity Type

Non Profit

Font styles to use
Serif

Requirements
Must have
• The project needs to have a place for a mailing label and stamp and our return address. It should also include lots of pictures, our logos, be fun, and eye-catching.
Nice to have
• pictures, logo, etc.

```html
<!DOCTYPE html>
<html lang="en">
<head>
<meta charset="utf-8">
<title>Interfaith Summer Flyer</title>
<link href="https://fonts.googleapis.com/css2?family=Jost:wght@600;700;800;900&display=swap" rel="stylesheet">
<style>
  :root {
    --sky: #1ea0e6;
    --sky-deep: #0f86d4;
    --sun: #ffd400;
    --sun-deep: #f7b500;
    --orange: #f59a1b;
    --red: #d42a2a;
    --blue-text: #1668c2;
    --navy: #1b3f8f;
    --white: #ffffff;
    --page: #ffffff;
    --photo-warm: #8a6a55;
    --photo-cool: #6d7e92;
  }
  * { margin: 0; padding: 0; box-sizing: border-box; }
  html, body { width: 1200px; height: 1200px; overflow: hidden; background: var(--page); }
  body { font-family: "Jost", "Futura", sans-serif; position: relative; }

  .flyer {
    position: absolute; left: 240px; top: 60px;
    width: 720px; height: 1080px; overflow: hidden;
    background: linear-gradient(180deg, var(--sky) 0%, var(--sky-deep) 70%);
  }
  .flyer-waves { position: absolute; inset: 0; }

  .photo {
    position: absolute;
    border: 6px solid var(--white);
    background: linear-gradient(135deg, var(--photo-warm), var(--photo-cool));
  }
  .photo--group-top { left: 47px; top: 47px; width: 625px; height: 215px; }
  .photo--group-bottom { left: 47px; top: 886px; width: 625px; height: 147px; }

  .snapshot-row {
    position: absolute; left: 83px; top: 490px; width: 560px; height: 142px;
    display: flex; gap: 8px;
  }
  .snapshot {
    flex: 1; border: 6px solid var(--white); border-radius: 14px;
    background: linear-gradient(150deg, #b08b76, #5f6470);
    box-shadow: 0 6px 0 rgba(0,0,0,0.15);
  }

  .join-tab {
    position: absolute; left: 292px; top: 0; width: 135px; height: 292px;
    background: linear-gradient(180deg, var(--sun) 0%, var(--sun-deep) 100%);
    border-radius: 0 0 10px 10px;
    box-shadow: 0 6px 0 rgba(0,0,0,0.12);
  }
  .tab-word {
    position: absolute; left: 0; width: 100%; text-align: center;
    color: var(--navy); font-weight: 800;
  }
  .tab-word--join { top: 38px; font-size: 38px; }
  .tab-word--for { top: 248px; font-size: 26px; font-weight: 700; }

  .org-mark {
    position: absolute; left: 249px; top: 100px; width: 222px; height: 127px;
    background: var(--white); border-radius: 12px;
    display: flex; align-items: center; justify-content: center; gap: 10px;
    padding: 0 14px;
  }
  .org-mark__name {
    color: var(--blue-text); font-weight: 600; font-size: 27px; line-height: 1.02;
  }
  .org-mark__dot {
    width: 40px; height: 40px; border-radius: 50%; background: var(--blue-text); flex: none;
  }

  .headline {
    position: absolute; left: 0; top: 300px; width: 100%; text-align: center;
    font-weight: 900; font-size: 82px; line-height: 0.92; letter-spacing: -1px;
    background: linear-gradient(180deg, #fff6a0 0%, var(--sun) 45%, var(--sun-deep) 100%);
    -webkit-background-clip: text; background-clip: text; color: transparent;
    filter: drop-shadow(0 4px 0 rgba(0,40,110,0.35));
  }

  .details {
    position: absolute; left: 0; top: 690px; width: 100%; text-align: center;
    font-weight: 800; font-size: 49px; line-height: 1.0; letter-spacing: -0.5px;
  }
  .details__trip { color: var(--red); }
  .details__program { color: var(--blue-text); }
</style>
</head>
<body>
  <main class="flyer">
    <svg class="flyer-waves" width="720" height="1080" viewBox="0 0 720 1080" aria-hidden="true">
      <path d="M0,452 C170,380 520,430 720,686 L720,1080 L0,1080 Z" fill="var(--orange)"/>
      <path d="M0,466 C170,398 515,446 720,700 L720,1080 L0,1080 Z" fill="var(--white)"/>
      <path d="M0,478 C170,412 510,460 720,714 L720,1080 L0,1080 Z" fill="var(--sun)"/>
    </svg>

    <div class="photo photo--group-top" role="img" aria-label="Large group of teen participants posing together indoors"></div>

    <div class="join-tab">
      <span class="tab-word tab-word--join">JOIN</span>
      <span class="tab-word tab-word--for">FOR AN</span>
    </div>
    <div class="org-mark">
      <span class="org-mark__name">Common Ground Allies</span>
      <span class="org-mark__dot"></span>
    </div>

    <h1 class="headline">INTERFAITH<br>SUMMER!</h1>

    <div class="snapshot-row">
      <div class="snapshot" role="img" aria-label="Two smiling teen participants"></div>
      <div class="snapshot" role="img" aria-label="Three friends posing together"></div>
      <div class="snapshot" role="img" aria-label="Group of teens making playful poses"></div>
    </div>

    <div class="details">
      <p class="details__trip">WASHINGTON DC TRIP</p>
      <p class="details__trip">JUNE 11-16</p>
      <p class="details__program">INTERFAITH YOUTH</p>
      <p class="details__program">LEADERSHIP INITIATIVE</p>
    </div>

    <div class="photo photo--group-bottom" role="img" aria-label="Youth leadership group photo in a hall"></div>
  </main>
</body>
</html>
```